Company Values Graphic

We are looking for a design of our company values that can be used in a variety of places including our website, mousepads, office posters, business cards, etc.

Notes:
- We'd rather have icons/art than photographs on the poster.... so more like an infographic
- The core value group headings are not required, but can be included if you think grouping the values works for your design
- We have a logo for our software product but that logo is not required
- We don't need/want clever images to accompany each value, but some images are fine
- BrisKel logo attached
- BrisKel colors are attached
- BrisKel logo is Nunito Sans ExtraBold 800
- BrisKel website uses Roboto

Our Values - Who we will work with (and who we will not)
The right set of values are essential to building and maintaining a culture that we all wake up eager to be a part of each day. They are foundational to all hiring and firing decisions. They attract the right people and repel the wrong ones.

BE HELPFUL
Make every person and place better because you are there.
Deliver wow with every interaction.

BE HUMBLE
Listen with every muscle.
Passionately help others first.
Seek first to understand.

BE HONEST
Earn trust every day.
Be open and direct.
Treat everyone with fairness and respect.

BE HUMAN
Celebrate passion and action.
Create an environment where people are authentic.
Hire great people and expect a lot from them

BE COURAGEOUS
Dare mighty things.
Make and honor commitments.
All great things start with a small act of courage applied at the right moment.

```html
<!DOCTYPE html>
<html lang="en">
<head>
<meta charset="utf-8">
<title>BrisKel Company Values</title>
<link rel="stylesheet" href="https://fonts.googleapis.com/css2?family=Montserrat:wght@400;800&family=Roboto:wght@400&family=Roboto+Condensed:wght@500&display=swap">
<style>
  :root {
    --backdrop: #b5b5b5;
    --paper: #ffffff;
    --amber: #f7941d;
    --flame: #ef4123;
    --red: #e4202a;
    --red-orange: #e93a26;
    --orange: #f05a28;
    --tangerine: #f37021;
    --panel-edge: #4a4a4a;
    --ink: #1a1a1a;
    --body-ink: #2b2b2b;
  }
  html, body {
    margin: 0;
    width: 800px;
    height: 1200px;
    overflow: hidden;
    background: var(--backdrop);
  }
  .values-card {
    position: absolute;
    left: 20px;
    top: 306px;
    width: 760px;
    height: 588px;
    box-shadow: 3px 4px 8px rgba(0,0,0,0.25);
    background: var(--paper);
  }
  .values-card svg { display: block; width: 100%; height: 100%; }
  .title-bold { font-family: "Montserrat", sans-serif; font-weight: 800; fill: #fff; }
  .title-light { font-family: "Montserrat", sans-serif; font-weight: 400; fill: #fff; }
  .intro { font-family: "Roboto", sans-serif; font-size: 17px; fill: #fff; }
  .value-text { font-family: "Roboto", sans-serif; font-size: 17px; fill: var(--body-ink); }
  .value-label { font-family: "Montserrat", sans-serif; font-weight: 800; font-size: 24px; fill: #fff; letter-spacing: 0.5px; }
  .value-number { font-family: "Roboto Condensed", sans-serif; font-weight: 500; font-size: 27px; fill: #fff; }
  .brand-name { font-family: "Montserrat", sans-serif; font-weight: 800; font-size: 48px; fill: var(--ink); }
</style>
</head>
<body>
<div class="values-card">
<svg viewBox="0 0 1147 888" xmlns="http://www.w3.org/2000/svg">
  <defs>
    <linearGradient id="header-fade" x1="0" y1="0" x2="0" y2="1">
      <stop offset="0" stop-color="var(--amber)"/>
      <stop offset="1" stop-color="var(--flame)"/>
    </linearGradient>
    <linearGradient id="panel-fade" x1="0" y1="0" x2="1" y2="0">
      <stop offset="0" stop-color="#ffffff"/>
      <stop offset="1" stop-color="#e9e9eb"/>
    </linearGradient>
    <linearGradient id="fold-shade" x1="0" y1="0" x2="1" y2="1">
      <stop offset="0" stop-color="#000" stop-opacity="0"/>
      <stop offset="1" stop-color="#000" stop-opacity="0.22"/>
    </linearGradient>
    <linearGradient id="drop-shadow" x1="0" y1="0" x2="0" y2="1">
      <stop offset="0" stop-color="#000" stop-opacity="0.12"/>
      <stop offset="1" stop-color="#000" stop-opacity="0"/>
    </linearGradient>
  </defs>

  <!-- header -->
  <g class="header">
    <rect width="1147" height="208" fill="url(#header-fade)"/>
    <text class="title-bold" x="573" y="77" font-size="50" text-anchor="middle">WHO WE WILL WORK WITH</text>
    <text class="title-light" x="573" y="127" font-size="48" text-anchor="middle">(AND WHO WE WILL NOT)</text>
    <text class="intro" x="573" y="152" text-anchor="middle">The right set of values are essential to building and maintaining a culture that we all wake up eager to be a part of each day.</text>
    <text class="intro" x="573" y="174" text-anchor="middle">They are foundational to all hiring and firing decisions. They attract the right people and repel the wrong ones.</text>
  </g>

  <!-- value rows -->
  <g class="value-row">
    <polygon points="1004,260 1087,312 1087,390 1020,400 960,332" fill="url(#drop-shadow)"/>
    <rect x="0" y="240" width="711" height="116" fill="url(#panel-fade)"/>
    <line x1="0" y1="240" x2="711" y2="240" stroke="var(--panel-edge)" stroke-width="1.5"/>
    <text class="value-text" x="640" y="289" text-anchor="end">Make every person and place better because you are there.</text>
    <text class="value-text" x="640" y="310" text-anchor="end">Deliver wow with every interaction.</text>
    <rect x="711" y="260" width="293" height="72" fill="var(--red)"/>
    <polygon points="1004,260 1087,312 1029,312 946,332 1004,332" fill="var(--red)"/>
    <polygon points="946,332 1004,332 1029,312 1029,378" fill="var(--red)"/>
    <polygon points="944,332 1029,312 1029,378" fill="url(#fold-shade)"/>
    <rect x="1029" y="312" width="58" height="66" fill="var(--red)"/>
    <rect x="1029" y="312" width="58" height="66" fill="#000" opacity="0.08"/>
    <text class="value-label" x="767" y="303">BE HELPFUL</text>
    <text class="value-number" x="1058" y="354" text-anchor="middle">01</text>
  </g>

  <g class="value-row">
    <polygon points="926,376 1009,428 1009,506 942,516 882,448" fill="url(#drop-shadow)"/>
    <rect x="0" y="359" width="633" height="116" fill="url(#panel-fade)"/>
    <line x1="0" y1="359" x2="633" y2="359" stroke="var(--panel-edge)" stroke-width="1.5"/>
    <text class="value-text" x="578" y="410" text-anchor="end">Listen with every muscle. Passionately help others first.</text>
    <text class="value-text" x="578" y="431" text-anchor="end">Seek first to understand.</text>
    <rect x="633" y="376" width="293" height="72" fill="var(--red-orange)"/>
    <polygon points="926,376 1009,428 951,428 868,448 926,448" fill="var(--red-orange)"/>
    <polygon points="868,448 951,428 951,494" fill="var(--red-orange)"/>
    <polygon points="866,448 951,428 951,494" fill="url(#fold-shade)"/>
    <rect x="951" y="428" width="58" height="66" fill="var(--red-orange)"/>
    <rect x="951" y="428" width="58" height="66" fill="#000" opacity="0.08"/>
    <text class="value-label" x="694" y="420">BE HUMBLE</text>
    <text class="value-number" x="980" y="470" text-anchor="middle">02</text>
  </g>

  <g class="value-row">
    <polygon points="848,492 931,544 931,622 864,632 804,564" fill="url(#drop-shadow)"/>
    <rect x="0" y="476" width="556" height="114" fill="url(#panel-fade)"/>
    <line x1="0" y1="476" x2="556" y2="476" stroke="var(--panel-edge)" stroke-width="1.5"/>
    <text class="value-text" x="499" y="525" text-anchor="end">Earn trust every day. Be open and direct.</text>
    <text class="value-text" x="499" y="546" text-anchor="end">Treat everyone with fairness and respect.</text>
    <rect x="556" y="492" width="292" height="72" fill="var(--orange)"/>
    <polygon points="848,492 931,544 873,544 790,564 848,564" fill="var(--orange)"/>
    <polygon points="790,564 873,544 873,610" fill="var(--orange)"/>
    <polygon points="788,564 873,544 873,610" fill="url(#fold-shade)"/>
    <rect x="873" y="544" width="58" height="66" fill="var(--orange)"/>
    <rect x="873" y="544" width="58" height="66" fill="#000" opacity="0.08"/>
    <text class="value-label" x="616" y="536">BE HONEST</text>
    <text class="value-number" x="902" y="586" text-anchor="middle">03</text>
  </g>

  <g class="value-row">
    <polygon points="770,607 853,659 853,737 786,747 726,679" fill="url(#drop-shadow)"/>
    <rect x="0" y="590" width="478" height="116" fill="url(#panel-fade)"/>
    <line x1="0" y1="590" x2="478" y2="590" stroke="var(--panel-edge)" stroke-width="1.5"/>
    <text class="value-text" x="429" y="630" text-anchor="end">Celebrate passion and action. Create an</text>
    <text class="value-text" x="429" y="651" text-anchor="end">environment where people are authentic.</text>
    <text class="value-text" x="429" y="672" text-anchor="end">Hire great people and expect a lot from them</text>
    <rect x="478" y="607" width="292" height="72" fill="var(--tangerine)"/>
    <polygon points="770,607 853,659 795,659 712,679 770,679" fill="var(--tangerine)"/>
    <polygon points="712,679 795,659 795,725" fill="var(--tangerine)"/>
    <polygon points="710,679 795,659 795,725" fill="url(#fold-shade)"/>
    <rect x="795" y="659" width="58" height="66" fill="var(--tangerine)"/>
    <rect x="795" y="659" width="58" height="66" fill="#000" opacity="0.08"/>
    <text class="value-label" x="547" y="651">BE HUMAN</text>
    <text class="value-number" x="824" y="701" text-anchor="middle">04</text>
  </g>

  <g class="value-row">
    <polygon points="692,723 775,775 775,853 708,863 648,795" fill="url(#drop-shadow)"/>
    <rect x="0" y="706" width="401" height="114" fill="url(#panel-fade)"/>
    <line x1="0" y1="706" x2="401" y2="706" stroke="var(--panel-edge)" stroke-width="1.5"/>
    <text class="value-text" x="354" y="737" text-anchor="end">Dare mighty things.</text>
    <text class="value-text" x="354" y="758" text-anchor="end">Make and honor commitments.</text>
    <text class="value-text" x="354" y="779" text-anchor="end">All great things start with a small act of</text>
    <text class="value-text" x="354" y="800" text-anchor="end">courage applied at the right moment.</text>
    <rect x="401" y="723" width="291" height="72" fill="var(--amber)"/>
    <polygon points="692,723 775,775 717,775 634,795 692,795" fill="var(--amber)"/>
    <polygon points="634,795 717,775 717,841" fill="var(--amber)"/>
    <polygon points="632,795 717,775 717,841" fill="url(#fold-shade)"/>
    <rect x="717" y="775" width="58" height="66" fill="var(--amber)"/>
    <rect x="717" y="775" width="58" height="66" fill="#000" opacity="0.08"/>
    <text class="value-label" x="439" y="769">BE COURAGEOUS</text>
    <text class="value-number" x="746" y="817" text-anchor="middle">05</text>
  </g>

  <!-- brand -->
  <g class="brand">
    <circle cx="962" cy="720" r="26" fill="var(--flame)"/>
    <text class="brand-name" x="962" y="808" text-anchor="middle">BrisKel</text>
  </g>

  <!-- footer stripes -->
  <g class="footer-stripes">
    <rect x="0" y="862" width="376" height="26" fill="var(--red)"/>
    <rect x="386" y="862" width="375" height="26" fill="var(--orange)"/>
    <rect x="771" y="862" width="376" height="26" fill="var(--amber)"/>
  </g>
</svg>
</div>
</body>
</html>
```